Your Brimtoral App all-in-one system for transformation needs a book cover.

Hello- I would like a very similar book cover ( Under Quiet Lanterns book cover) as the sample I'm attaching. The person on my book cover would be less stiff, wear a cowboy hat, and maybe have flying hair. High-end bohemian style. Our brand colors are gold, light pink, and tan color. I'll attach App Logo and the colors we used on that. The title of my book is: "The Radiant Harvest Pathway" and I will also need formatting for ebook, audio, and paperback. Thank you, Maribel

Target Market(s)

Those who are on the path to enlightenment - 60% women 40% men

Industry/Entity Type

Consciousness Industry

Font styles to use
Other font styles liked:
• Dubai

Colors
0054AA
0677BA
7BADD7
CADEEF
E8F1F8
FFC000
F8CF3A
FAE287
FDF2CF
FEFAEE
F0912C
F2A743
F7CA91
FBE8D2
FDF5EE
EE7325
F08F49
F5BC92
FAE3D3
FDF4ED
6B429C
8869AF
B7A5CE
E3DAEB
F3F0F8

Requirements
Must have
• Light spheres - light pink, orange-pink, gold and possibly blue on the very top
Should not have
• More of a sun rise feel, less or no clouds in the upper section,

```html
<!DOCTYPE html>
<html lang="en">
<head>
<meta charset="utf-8">
<title>The Radiant Harvest Pathway — Book Cover</title>
<link rel="stylesheet" href="https://fonts.googleapis.com/css2?family=Jost:wght@600&display=swap">
<style>
  :root {
    --sky-violet: #5e5496;
    --sky-purple: #785c9e;
    --sky-mauve: #a86f9f;
    --sky-rose: #e08f9f;
    --cloud-pink: rgba(232, 160, 190, 0.75);
    --horizon-peach: #f9d6bc;
    --horizon-glow: #fff5dc;
    --sun-core: #fffdf2;
    --field-amber: #a9503a;
    --field-rust: #7c3128;
    --field-deep: #561d1f;
    --figure-plum: rgba(96, 34, 52, 0.92);
    --figure-ember: rgba(190, 70, 60, 0.75);
    --title-cream: rgba(250, 240, 226, 0.93);
  }
  html, body {
    margin: 0;
    padding: 0;
    width: 800px;
    height: 1200px;
    overflow: hidden;
    background: var(--sky-violet);
  }
  .book-cover {
    position: relative;
    width: 800px;
    height: 1200px;
    overflow: hidden;
  }
  .sky-backdrop {
    position: absolute;
    inset: 0;
    background:
      radial-gradient(ellipse 110px 150px at 770px 230px, var(--cloud-pink) 0%, rgba(232,160,190,0) 100%),
      radial-gradient(ellipse 220px 140px at 60px 170px, rgba(225,120,150,0.7) 0%, rgba(225,120,150,0) 100%),
      radial-gradient(ellipse 260px 120px at 130px 20px, rgba(215,140,175,0.6) 0%, rgba(215,140,175,0) 100%),
      radial-gradient(ellipse 300px 120px at 700px 640px, rgba(225,110,140,0.55) 0%, rgba(225,110,140,0) 100%),
      radial-gradient(circle 34px at 648px 878px, rgba(255,252,238,0.95) 0%, rgba(255,245,220,0) 100%),
      radial-gradient(circle 40px at 790px 845px, rgba(255,252,238,0.9) 0%, rgba(255,245,220,0) 100%),
      radial-gradient(ellipse 560px 300px at 400px 880px, var(--horizon-glow) 0%, rgba(252,228,200,0.65) 45%, rgba(240,190,190,0) 100%),
      linear-gradient(to bottom,
        var(--sky-violet) 0%,
        var(--sky-purple) 28%,
        var(--sky-mauve) 46%,
        var(--sky-rose) 56%,
        var(--horizon-peach) 66%,
        var(--horizon-glow) 76%);
  }
  .figure-area {
    position: absolute;
    left: 255px;
    top: 545px;
    width: 210px;
    height: 450px;
    border-radius: 50% 50% 40% 40% / 18% 18% 30% 30%;
    background: linear-gradient(to bottom,
      var(--figure-plum) 0%,
      rgba(110,36,50,0.88) 35%,
      var(--figure-ember) 65%,
      rgba(255,220,190,0.15) 100%);
    filter: blur(6px);
  }
  .ground {
    position: absolute;
    left: 0;
    top: 0;
    width: 800px;
    height: 1200px;
  }
  .sun-flare {
    position: absolute;
    left: 230px;
    top: 930px;
    width: 180px;
    height: 140px;
    border-radius: 50%;
    background: radial-gradient(ellipse at center, var(--sun-core) 0%, rgba(255,248,225,0.7) 35%, rgba(255,240,210,0) 70%);
  }
  .cover-title {
    position: absolute;
    left: 0;
    right: 0;
    top: 116px;
    margin: 0;
    text-align: center;
    font-family: "Jost", "Futura", sans-serif;
    font-weight: 600;
    font-size: 104px;
    line-height: 119px;
    letter-spacing: 0.12em;
    text-transform: uppercase;
    color: var(--title-cream);
  }
  .cover-title .title-line {
    display: block;
    padding-left: 0.12em;
    white-space: nowrap;
  }
</style>
</head>
<body>
  <main class="book-cover" role="img" aria-label="Sunrise over a grassy hill with a purple and pink sky, glowing light spheres, and a bohemian woman in a wide-brimmed hat walking away with hair blowing in the wind">
    <div class="sky-backdrop"></div>
    <div class="figure-area" role="img" aria-label="Silhouette of a woman in a hat and flowing dress walking toward the sunrise"></div>
    <svg class="ground" viewBox="0 0 800 1200" aria-hidden="true">
      <defs>
        <linearGradient id="field-fill" x1="0" y1="0" x2="0" y2="1">
          <stop offset="0" stop-color="#a9503a"/>
          <stop offset="0.35" stop-color="#7c3128"/>
          <stop offset="1" stop-color="#561d1f"/>
        </linearGradient>
      </defs>
      <path d="M0 915 C120 925 230 975 330 992 C420 1000 520 960 620 935 C700 918 760 914 800 912 L800 1200 L0 1200 Z" fill="url(#field-fill)"/>
    </svg>
    <div class="sun-flare"></div>
    <h1 class="cover-title">
      <span class="title-line">The</span>
      <span class="title-line">Radiant</span>
      <span class="title-line">Harvest</span>
      <span class="title-line">Pathway</span>
    </h1>
  </main>
</body>
</html>
```